NEW STORE PROMOTION FLYER

We need a flyer design for a new lingerie store based in Double Bay.
The people living in Double Bay are most wealthy suburb in Sydney. Our customers are aged at 30+ to 70.
We are offering 'up to 30% off' on selected products.
we recommend using our theme colour: light pink, red, white
the address is:
shop 5/214 Marlow Crest Rd, NSW 2173
contact number: 02 8415 3907
We need key information:
1. we want to let neighborhood know that we open a new store.
2. we offer 'up to 30% off' Christmas Sale
3. Please use our theme colour: light pink, red, white
4. Please add the address map on flyer (you may design again if you need )
5.open hour:
Mon - Fri 10:00am - 5:30pm
Sat - Sun 10:00am - 5:30pm
thank you
aged 30+ to 70; they are relatively wealthy.
Store

```html
<!DOCTYPE html>
<html lang="en">
<head>
<meta charset="utf-8">
<title>Lunamae Lingerie – Christmas Sale</title>
<link href="https://fonts.googleapis.com/css2?family=Anton&family=Archivo:wght@700;800&family=Tinos&display=swap" rel="stylesheet">
<style>
  :root {
    --magenta: #d6199c;
    --magenta-deep: #c2127f;
    --pink-light: #f6c9e3;
    --pink-mid: #eca4cf;
    --pink-ray: #e78cc4;
    --white: #ffffff;
    --ink: #1a1a1a;
    --shadow: rgba(90, 20, 60, 0.45);
  }
  * { margin: 0; padding: 0; box-sizing: border-box; }
  html, body { width: 800px; height: 1200px; overflow: hidden; background: var(--white); }
  .flyer {
    position: relative;
    width: 800px;
    height: 1200px;
    overflow: hidden;
    background: radial-gradient(ellipse at 50% 55%, var(--pink-light) 0%, var(--pink-mid) 55%, var(--pink-ray) 100%);
    font-family: "Anton", "Arial Narrow", sans-serif;
  }
  .backdrop {
    position: absolute; inset: 0 0 450px 0;
  }
  .brand {
    position: absolute; top: 30px; left: 0; width: 800px;
    text-align: center; color: var(--magenta);
    font-family: "Anton", sans-serif;
  }
  .brand-name { font-size: 130px; line-height: 1; letter-spacing: 4px; }
  .brand-line { font-size: 48px; line-height: 1.1; letter-spacing: 24px; margin-top: 14px; padding-left: 24px; }
  .rule {
    position: absolute; left: 0; width: 800px; height: 5px; background: var(--magenta);
  }
  .rule.top { top: 289px; }
  .rule.bottom { top: 751px; }
  .offer-up-to {
    position: absolute; left: 42px; top: 596px;
    transform-origin: left top; transform: rotate(-90deg);
    color: var(--white); font-size: 110px; line-height: 1; letter-spacing: 7px;
    text-shadow: 4px 4px 6px var(--shadow);
    white-space: nowrap;
  }
  .offer-figure {
    position: absolute; left: 157px; top: 322px;
    color: var(--magenta); font-size: 290px; line-height: 1; letter-spacing: -4px;
    transform-origin: left top; transform: scaleX(0.8);
    text-shadow: 5px 5px 0 var(--magenta-deep), 9px 10px 12px var(--shadow);
    white-space: nowrap;
  }
  .offer-off {
    position: absolute; left: 632px; top: 348px;
    color: var(--white); font-size: 90px; line-height: 1;
    text-shadow: 4px 4px 6px var(--shadow);
  }
  .offer-title {
    position: absolute; left: 0; top: 624px; width: 800px; text-align: center;
    color: var(--white); font-size: 108px; line-height: 1; letter-spacing: 1px;
    transform: skewX(-12deg);
    text-shadow: 5px 6px 6px var(--shadow);
  }
  .contact {
    position: absolute; left: 0; top: 789px; width: 800px; height: 108px;
    background: var(--white); color: var(--magenta);
    font-family: "Archivo", sans-serif; font-weight: 800;
    text-align: center; font-size: 33px; line-height: 50px; padding-top: 4px;
    text-transform: uppercase;
  }
  .footer {
    position: absolute; left: 0; top: 901px; width: 800px; height: 299px;
    background: linear-gradient(180deg, #f06fc0 0%, var(--magenta) 100%);
  }
  .hours {
    position: absolute; left: 20px; top: 22px; width: 440px;
    color: var(--white); text-align: center;
    font-family: "Archivo", sans-serif; font-weight: 700;
    font-size: 46px; line-height: 64px;
  }
  .map-card {
    position: absolute; left: 469px; top: 19px; width: 318px; height: 267px;
    background: var(--white); border: 2px solid var(--ink);
  }
  .map-area {
    position: absolute; left: 6px; top: 6px; width: 302px; height: 222px;
    background: linear-gradient(160deg, #f4f4f4 0%, #e2e2e2 100%);
  }
  .map-caption {
    position: absolute; left: 0; bottom: 8px; width: 100%; text-align: center;
    font-family: "Tinos", "Times New Roman", serif; font-size: 16px; color: var(--ink);
  }
</style>
</head>
<body>
  <main class="flyer">
    <div class="backdrop" role="img" aria-label="Pink sunburst rays radiating from the centre"></div>

    <header class="brand">
      <div class="brand-name">Lunamae</div>
      <div class="brand-line">Lingerie</div>
    </header>

    <div class="rule top"></div>

    <section class="offer">
      <div class="offer-up-to">UP TO</div>
      <div class="offer-figure">30%</div>
      <div class="offer-off">OFF</div>
      <div class="offer-title">CHRISTMAS SALE!</div>
    </section>

    <div class="rule bottom"></div>

    <section class="contact">
      <p>Shop 5/214 Marlow Crest Rd, NSW 2173</p>
      <p>Contact number: 02 8415 3907</p>
    </section>

    <section class="footer">
      <div class="hours">
        <p>MON- FRI</p>
        <p>10:00AM - 5:30PM</p>
        <p>SAT - SUN</p>
        <p>10:00AM - 5:30PM</p>
      </div>
      <div class="map-card">
        <div class="map-area" role="img" aria-label="Street map showing the store location near the main road"></div>
        <p class="map-caption">Shop 5/ 214 Marlow Crest Rd, NSW 2173</p>
      </div>
    </section>
  </main>
</body>
</html>
```